Elegant Black Candle Label Design!

I need a 2.375" tall by 3.0" wide candle label design. I'm looking for simple and elegant. Black label with silver leaf border and lettering. Label needs to have the following information on it: Fern Hollow Candle Co. as the company name, scent name in the middle and in smaller font, it needs to say Made in USA, All Natural, 8oz. Attached photos are for inspiration.

Target Market(s)

People looking for high end, all natural candle fragrances

Industry/Entity Type

Candle-Spa

Colors

Designer to choose only greyscale colors for use in the design.

Requirements
Must have
• Company Name, Scent (ability to change scent names), All Natural, Made in USA, 8oz
Nice to have
• Black background, silver leaf border and silver leaf font. Elegant fonts maybe slightly cursive

```html
<!DOCTYPE html>
<html lang="en">
<head>
<meta charset="utf-8">
<title>Fern Hollow Candle Co. – Soy Candle Label</title>
<link rel="stylesheet" href="https://fonts.googleapis.com/css2?family=Marcellus&family=Josefin+Sans:wght@400&display=swap">
<style>
  :root {
    --backdrop: #2e2e2e;
    --label: #1e1e1e;
    --silver: #dcdcdc;
    --silver-dark: #8f8f8f;
    --ink: #2a2a2a;
  }
  * { margin: 0; padding: 0; box-sizing: border-box; }
  html, body {
    width: 1200px;
    height: 960px;
    overflow: hidden;
    background: var(--backdrop);
  }
  .label {
    position: absolute;
    left: 30px;
    top: 30px;
    width: 1140px;
    height: 900px;
    background: var(--label);
    color: var(--silver);
    font-family: "Marcellus", serif;
  }
  .label__frame {
    position: absolute;
    inset: 0;
    width: 1140px;
    height: 900px;
  }
  .label__frame polygon {
    fill: none;
    stroke: var(--silver);
    stroke-width: 2.5;
  }
  .brand {
    position: absolute;
    left: 190px;
    top: 268px;
    width: 700px;
    font-family: "Marcellus", serif;
    font-weight: 400;
    color: var(--silver);
  }
  .brand__name {
    display: block;
    font-size: 84px;
    line-height: 1;
    letter-spacing: 1px;
  }
  .brand__suffix {
    display: block;
    font-size: 34px;
    letter-spacing: 10px;
    text-transform: uppercase;
    text-align: right;
    margin-top: 22px;
    padding-right: 6px;
  }
  .leaf-sprig {
    position: absolute;
    border-radius: 50%;
    background: radial-gradient(ellipse at center, rgba(220,220,220,0.35), rgba(220,220,220,0.06) 70%, transparent 75%);
  }
  .leaf-sprig--top { left: 872px; top: 246px; width: 122px; height: 150px; }
  .leaf-sprig--bottom { left: 212px; top: 688px; width: 326px; height: 200px; }
  .scent-band {
    position: absolute;
    left: 212px;
    top: 492px;
    width: 722px;
    height: 54px;
    background: linear-gradient(90deg, var(--silver-dark), #f2f2f2 30%, #bdbdbd 55%, #ffffff 80%, #d0d0d0);
    display: flex;
    align-items: center;
    justify-content: center;
  }
  .scent-band__name {
    font-family: "Marcellus", serif;
    font-size: 32px;
    line-height: 1;
    letter-spacing: 5px;
    color: var(--ink);
    text-transform: uppercase;
  }
  .details {
    position: absolute;
    left: 180px;
    top: 620px;
    width: 780px;
    display: flex;
    justify-content: space-between;
    list-style: none;
    font-family: "Josefin Sans", sans-serif;
    font-size: 27px;
    letter-spacing: 1px;
    text-transform: uppercase;
    color: var(--silver);
  }
  .details__item { width: 260px; text-align: center; }
</style>
</head>
<body>
  <main class="label">
    <svg class="label__frame" viewBox="0 0 1140 900" aria-hidden="true">
      <polygon points="68,79 1075,82 1077,837 72,830"/>
      <polygon points="78,97 1070,70 1088,828 85,847"/>
    </svg>

    <div class="leaf-sprig leaf-sprig--top" role="img" aria-label="Silver leaf sprig ornament"></div>

    <h1 class="brand">
      <span class="brand__name">Fern Hollow</span>
      <span class="brand__suffix">Candle Co.</span>
    </h1>

    <div class="scent-band">
      <span class="scent-band__name">Soy Candle</span>
    </div>

    <ul class="details">
      <li class="details__item">All Natural</li>
      <li class="details__item">8oz</li>
      <li class="details__item">Made in USA</li>
    </ul>

    <div class="leaf-sprig leaf-sprig--bottom" role="img" aria-label="Silver leafy branch ornament"></div>
  </main>
</body>
</html>
```